Car Wrap Design for Parquet Company

We are a parquet retailer and parquet laying company from Germany. We need a car wrap design for our van. It should have a noticeable design and so be modern and look premium. Enclosed we present you three favorite designs from other companys. We especially like favorite1. We like the theme wood in the design. We'd like to hear the follwing in the advertisement: - Over 25 years experience (more that 25 years of experience) - Birch to Wenge (our slogan) quality - www.Dielen-Warnke.example (our website) - 0913 - 72 15 904 (our telephone number) Our van is a Varlo K420 M3T3. Enclosed you find some pictures and the dimensions.
Colors
Designer to choose colors to be used in the design.
Look and feel
Each slider illustrates characteristics of the customer's brand and the style your logo design should communicate.

```html
<!DOCTYPE html>
<html lang="de">
<head>
<meta charset="utf-8">
<title>Dielen Warnke – Van Wrap Sheet</title>
<link href="https://fonts.googleapis.com/css2?family=Montserrat:ital,wght@0,500;0,600;0,700;1,500&display=swap" rel="stylesheet">
<style>
  :root{
    --paper:#ffffff;
    --wood-dark:#4a3a2e;
    --wood-mid:#7a6656;
    --wood-light:#b9a892;
    --walnut:#8a3f17;
    --copper:#c8692a;
    --forest:#1f3a1e;
    --sage:#5b7f4c;
    --cream:#f4f2ee;
    --ink:#111111;
    --line:#3a3a3a;
  }
  *{margin:0;padding:0;box-sizing:border-box}
  html,body{width:1200px;height:1000px;overflow:hidden;background:var(--paper)}
  body{font-family:"Montserrat",sans-serif;color:var(--ink)}
  .canvas{position:relative;width:1200px;height:1000px}
  .wood{position:absolute;background:linear-gradient(90deg,var(--wood-mid),var(--wood-light) 18%,var(--wood-dark) 36%,var(--wood-light) 54%,var(--wood-mid) 72%,var(--wood-light) 88%,var(--wood-dark));border:1px solid var(--line);overflow:hidden}
  .wood.horizontal{background:linear-gradient(180deg,var(--wood-mid),var(--wood-light) 25%,var(--wood-dark) 50%,var(--wood-light) 75%,var(--wood-mid))}
  .shape{position:absolute}
  .badge{position:absolute;text-align:center}
  .brand-name{font-weight:600;color:var(--copper);line-height:1;letter-spacing:.12em}
  .claim{font-style:italic;font-weight:500;color:var(--ink)}
  .claim b{color:var(--sage);font-weight:700}
  .claim-bar{margin:3px auto 0;height:5px;background:var(--sage);border-radius:1px}
  .web{font-weight:700;color:var(--ink)}
  .slogan{position:absolute;color:var(--paper);font-weight:700;font-size:19px;line-height:1.3}
  .phone{position:absolute;color:var(--paper);font-weight:700;font-size:11px;display:flex;align-items:center;gap:6px}
  .vehicle{position:absolute;border-radius:10px}
</style>
</head>
<body>
<div class="canvas">

  <svg width="0" height="0" style="position:absolute">
    <defs>
      <polygon id="step-blob" points="30,0 70,0 70,5 80,5 80,12 88,12 88,22 95,22 95,35 100,35 100,65 95,65 95,78 88,78 88,88 80,88 80,95 70,95 70,100 30,100 30,95 20,95 20,88 12,88 12,78 5,78 5,65 0,65 0,35 5,35 5,22 12,22 12,12 20,12 20,5 30,5"/>
    </defs>
  </svg>

  <!-- Side panel, driver side -->
  <div class="wood" role="img" aria-label="Vertical parquet plank texture in brown and beige" style="left:46px;top:68px;width:566px;height:272px"></div>
  <svg class="shape" style="left:48px;top:198px" width="150" height="95" viewBox="0 0 100 100" preserveAspectRatio="none"><use href="#step-blob" fill="var(--forest)"/></svg>
  <svg class="shape" style="left:465px;top:110px" width="150" height="230" viewBox="0 0 100 100" preserveAspectRatio="none"><use href="#step-blob" fill="var(--walnut)"/></svg>
  <svg class="shape" style="left:215px;top:95px" width="232" height="210" viewBox="0 0 100 100" preserveAspectRatio="none"><use href="#step-blob" fill="var(--cream)"/></svg>
  <div class="badge" style="left:215px;top:146px;width:232px">
    <div class="brand-name" style="font-size:19px">DIELEN<br>WARNKE</div>
    <div class="claim" style="font-size:12px;margin-top:16px">Over <b>25</b> years experience</div>
    <div class="claim-bar" style="width:160px"></div>
    <div class="web" style="font-size:10px;margin-top:23px">www.Dielen-Warnke.example</div>
  </div>
  <div class="phone" style="left:56px;top:239px">
    <svg width="9" height="11" viewBox="0 0 24 24"><path fill="#fff" d="M6.6 10.8a15 15 0 0 0 6.6 6.6l2.2-2.2a1 1 0 0 1 1-.25 11.4 11.4 0 0 0 3.6.57 1 1 0 0 1 1 1V20a1 1 0 0 1-1 1A17 17 0 0 1 3 4a1 1 0 0 1 1-1h3.5a1 1 0 0 1 1 1c0 1.25.2 2.45.57 3.57a1 1 0 0 1-.25 1z"/></svg>
    0913 - 72 15 904
  </div>
  <div class="slogan" style="left:502px;top:193px">Birch<br>to<br>Wenge</div>

  <!-- Side panel, passenger side -->
  <div class="wood" role="img" aria-label="Vertical parquet plank texture in brown and beige" style="left:46px;top:382px;width:568px;height:273px"></div>
  <svg class="shape" style="left:46px;top:420px" width="140" height="235" viewBox="0 0 100 100" preserveAspectRatio="none"><use href="#step-blob" fill="var(--walnut)"/></svg>
  <svg class="shape" style="left:468px;top:518px" width="146" height="102" viewBox="0 0 100 100" preserveAspectRatio="none"><use href="#step-blob" fill="var(--forest)"/></svg>
  <svg class="shape" style="left:215px;top:395px" width="245" height="245" viewBox="0 0 100 100" preserveAspectRatio="none"><use href="#step-blob" fill="var(--cream)"/></svg>
  <div class="badge" style="left:215px;top:462px;width:245px">
    <div class="brand-name" style="font-size:21px">DIELEN<br>WARNKE</div>
    <div class="claim" style="font-size:13px;margin-top:14px">Over <b>25</b> years experience</div>
    <div class="claim-bar" style="width:185px"></div>
    <div class="web" style="font-size:11px;margin-top:20px">www.Dielen-Warnke.example</div>
  </div>
  <div class="slogan" style="left:91px;top:504px">Birch<br>to<br>Wenge</div>
  <div class="phone" style="left:478px;top:558px">
    <svg width="9" height="11" viewBox="0 0 24 24"><path fill="#fff" d="M6.6 10.8a15 15 0 0 0 6.6 6.6l2.2-2.2a1 1 0 0 1 1-.25 11.4 11.4 0 0 0 3.6.57 1 1 0 0 1 1 1V20a1 1 0 0 1-1 1A17 17 0 0 1 3 4a1 1 0 0 1 1-1h3.5a1 1 0 0 1 1 1c0 1.25.2 2.45.57 3.57a1 1 0 0 1-.25 1z"/></svg>
    0913 - 72 15 904
  </div>

  <!-- Roof panel -->
  <div class="wood" role="img" aria-label="Plain vertical parquet plank texture for the roof" style="left:42px;top:686px;width:568px;height:259px"></div>

  <!-- Van views -->
  <div class="vehicle" role="img" aria-label="Technical side view of the wrapped van, driver side, with dimensions" style="left:655px;top:30px;width:260px;height:150px;background:linear-gradient(90deg,#e8e8e8 0 8%,var(--wood-mid) 8%,var(--wood-light) 50%,var(--walnut) 92%,#e8e8e8 92%)"></div>
  <div class="vehicle" role="img" aria-label="Technical side view of the wrapped van, passenger side, with dimensions" style="left:655px;top:200px;width:262px;height:150px;background:linear-gradient(90deg,#e8e8e8 0 6%,var(--walnut) 6%,var(--wood-light) 45%,var(--wood-mid) 78%,var(--forest) 92%,#e8e8e8 92%)"></div>
  <div class="vehicle" role="img" aria-label="Technical top view of the van with wrapped roof" style="left:650px;top:370px;width:265px;height:120px;background:linear-gradient(90deg,#eeeeee 0 5%,var(--wood-mid) 5%,var(--wood-light) 50%,var(--wood-mid) 75%,#eeeeee 75%)"></div>
  <div class="vehicle" role="img" aria-label="Technical front view of the van with wrapped bonnet strip" style="left:965px;top:205px;width:100px;height:145px;background:linear-gradient(180deg,#eeeeee 0 40%,var(--wood-mid) 40% 55%,#dddddd 55%)"></div>
  <div class="vehicle" role="img" aria-label="Wrapped bonnet strip detail" style="left:1085px;top:278px;width:80px;height:32px;border-radius:4px;background:linear-gradient(90deg,var(--wood-mid),var(--cream) 30%,var(--cream) 70%,var(--wood-mid))"></div>
  <div class="vehicle" role="img" aria-label="Technical rear view of the van with wrapped back doors" style="left:965px;top:355px;width:105px;height:145px;background:linear-gradient(180deg,var(--wood-mid) 0,var(--cream) 30%,var(--cream) 55%,var(--walnut) 75%,#dddddd 78%)"></div>

  <!-- Bonnet panel -->
  <div class="wood horizontal" role="img" aria-label="Horizontal parquet plank texture" style="left:688px;top:535px;width:180px;height:113px"></div>
  <svg class="shape" style="left:730px;top:548px" width="96" height="52" viewBox="0 0 100 100" preserveAspectRatio="none"><use href="#step-blob" fill="var(--cream)"/></svg>
  <div class="badge" style="left:730px;top:562px;width:96px">
    <div class="brand-name" style="font-size:9px">DIELEN<br>WARNKE</div>
  </div>

  <!-- Rear door panel -->
  <div class="wood" role="img" aria-label="Vertical parquet plank texture" style="left:781px;top:681px;width:264px;height:279px"></div>
  <svg class="shape" style="left:781px;top:725px" width="264" height="235" viewBox="0 0 100 100" preserveAspectRatio="none"><use href="#step-blob" fill="var(--walnut)"/></svg>
  <svg class="shape" style="left:795px;top:700px" width="236" height="240" viewBox="0 0 100 100" preserveAspectRatio="none"><use href="#step-blob" fill="var(--cream)"/></svg>
  <div class="badge" style="left:795px;top:763px;width:236px">
    <div class="brand-name" style="font-size:21px">DIELEN<br>WARNKE</div>
    <div class="claim" style="font-size:12px;margin-top:16px">Over <b>25</b> years experience</div>
    <div class="claim-bar" style="width:175px"></div>
    <div class="web" style="font-size:11px;margin-top:24px">www.Dielen-Warnke.example</div>
  </div>

</div>
</body>
</html>
```